New packaging company website**

We are looking for a new design for our corporate website (www.cratevendo.it). The theme must be made with Elementor and Crocoblock plugins. Currently the demo site can be reached at www.cratevendo.cloud

You can also check our current site for your reference www.cratevendo.it
We mainly deal with the resale of industrial containers for companies, most of our customers are B2B but also a good number of private customers. The site must therefore be accessible to all and the prices always visible even without registration or other.

Given the heterogeneity of our articles, we need a very clear shop page, with clearly visible filters and possibly with a list view and a table.

However, it does not have to be a simple ecommerce, we still want a site with many texts, spaces for product FAQs, tooltips on filters or attributes.

Target Market(s)

90% B2B

Coding

Coded - Design and coding required

Requirements
Must have
• beautiful, modern and captivating graphics. It must be a "full" site and not a flat one.
Nice to have
• We are undecided about the location of the main product menu.

If you leave the top bar with the icons and labels of the macro categories, as happens now on the live site and on the demo site.

Or if you want to insert the classic "all categories" on the top menu (https://lumberfay.qrivenso.com/demo-tools/demo/tools/ or https://www.havelintheme.com/wordpress/havel/shop30/)

Or if you want to take advantage of something more modern, such as the sidebar menu (https://www.havelintheme.com/wordpress/havel/shop10/ or https://www.havelintheme.com/wordpress/havel/shop19/)

```html
<!DOCTYPE html>
<html lang="en">
<head>
<meta charset="utf-8">
<title>Cratevendo – Industrial Containers</title>
<link href="https://fonts.googleapis.com/css2?family=Lato:wght@400;700;900&family=Orbitron:wght@700;900&display=swap" rel="stylesheet">
<style>
:root{
  --blue:#0f5b8b;
  --blue-dark:#0c4f7a;
  --yellow:#fdd000;
  --red:#c8201c;
  --green:#2e9a3a;
  --ink:#1d1d1d;
  --muted:#555;
  --grey-bg:#f4f4f4;
  --line:#dedede;
  --white:#fff;
}
*{box-sizing:border-box;margin:0;padding:0}
html,body{width:1200px;height:3219px;overflow:hidden}
body{font-family:'Lato',sans-serif;color:var(--ink);background:var(--white);position:relative}
.abs{position:absolute}
a{color:inherit;text-decoration:none}

.topbar{position:absolute;left:0;top:0;width:1200px;height:32px;background:var(--blue);color:#fff;font-size:12px;font-weight:700}
.topbar .login{left:770px;top:9px}
.topbar .lang{left:884px;top:9px}
.topbar .sep{left:927px;top:7px;width:1px;height:18px;background:rgba(255,255,255,.5)}
.topbar .social{left:948px;top:9px;display:flex;gap:12px}
.dot{width:14px;height:14px;border-radius:3px;background:#fff;display:block}
.dot.red{background:var(--red)}

.header{position:absolute;left:0;top:32px;width:1200px;height:102px;background:#fff}
.logo{left:112px;top:30px;display:flex;align-items:center;gap:10px}
.logo .mark{width:38px;height:38px;background:var(--green);border-radius:4px}
.logo .name{font-size:28px;font-weight:900;color:var(--blue);letter-spacing:.5px}
.nav{left:375px;top:49px;display:flex;gap:27px;font-size:13.5px;color:#333}
.nav .active{color:var(--green)}
.assist{left:950px;top:30px;display:flex;align-items:center;gap:8px}
.assist .t{font-size:10px;color:#555;line-height:1.2}
.assist .t b{display:block;font-size:12.5px;color:#222;font-weight:400}

.catbar{position:absolute;left:0;top:134px;width:1200px;height:47px;background:var(--blue)}
.allcat{left:110px;top:0;width:202px;height:47px;background:var(--yellow);display:flex;align-items:center;gap:16px;padding-left:24px;font-size:13.5px;font-weight:700}
.search{left:397px;top:6px;width:316px;height:34px;background:#fff;font-size:12px;padding:11px 14px;color:#444}
.searchcat{left:715px;top:6px;width:85px;height:34px;background:#fff;font-size:12px;padding:11px 12px;color:#444}
.searchbtn{left:800px;top:6px;width:40px;height:34px;background:var(--green);display:flex;align-items:center;justify-content:center}
.icons{left:984px;top:14px;display:flex;gap:22px;align-items:center;color:#fff;font-size:12px;font-weight:700}

.hero{position:absolute;left:0;top:181px;width:1200px;height:527px;background:linear-gradient(180deg,#bfe0f7 0%,#a7d2f1 55%,#6f9cc0 80%,#4c7fa8 100%)}
.hero .tanks{position:absolute;left:480px;top:150px;width:650px;height:300px;border-radius:30px 30px 6px 6px;background:linear-gradient(180deg,#2c8ce0,#0e5fb8)}
.hero h1{position:absolute;left:113px;top:138px;font-family:'Orbitron',sans-serif;font-weight:900;font-size:29px;letter-spacing:1px;color:#111}
.hero .from{left:113px;top:174px;font-size:13px}
.pricebox{left:112px;top:197px;width:236px;height:81px;background:var(--yellow);font-family:'Orbitron',sans-serif;font-weight:900;font-size:56px;line-height:81px;padding-left:12px}
.pricebox sup{font-size:24px;vertical-align:30px}
.hero .btn{left:112px;top:281px;width:118px;height:32px;background:var(--red);color:#fff;font-size:13px;font-weight:700;display:flex;align-items:center;justify-content:center}

.grey{position:absolute;left:0;top:708px;width:1200px;height:977px;background:var(--grey-bg)}
.feature{position:absolute;top:42px;width:232px;height:177px;background:#fff;border:2px solid #e8e8e8;text-align:center}
.feature svg{margin-top:30px}
.feature h3{font-size:18px;font-weight:700;margin-top:12px}
.feature p{font-size:13px;color:#333;margin-top:6px;line-height:1.4;padding:0 24px}
.sect-title{position:absolute;width:1200px;text-align:center;font-size:26px;font-weight:700;letter-spacing:.3px}
.cat{position:absolute;background:#fff;border:2px solid #e6e6e6;overflow:hidden}
.cat h4{position:absolute;left:24px;top:27px;font-size:17.5px;font-weight:700;z-index:2}
.cat ul{position:absolute;left:24px;top:62px;list-style:none;font-size:12.5px;color:#333;line-height:16.5px;z-index:2}
.cat .va{position:absolute;left:24px;font-size:13px;color:var(--red);text-decoration:underline;z-index:2}
.cat .ph{position:absolute;z-index:1}
.btn-red{position:absolute;background:var(--red);color:#fff;font-size:13px;font-weight:700;display:flex;align-items:center;justify-content:center}

.promo{position:absolute;left:0;top:1685px;width:1200px;height:500px;background:#fff}
.promo .side{position:absolute;top:0;width:370px;height:500px;background:linear-gradient(160deg,#d2d3db,#a9abbb)}
.promo .save{position:absolute;width:1200px;text-align:center;top:36px;font-size:13px;color:#777;font-weight:700;letter-spacing:.5px}
.promo .sub{position:absolute;width:1200px;text-align:center;top:55px;font-size:13px}
.promo .off{position:absolute;left:418px;top:80px;color:var(--red);font-weight:700;display:flex;align-items:baseline;gap:16px}
.promo .off .s{font-size:38px}
.promo .off .b{font-size:78px;font-weight:900}
.promo .shop{position:absolute;width:1200px;text-align:center;top:173px;font-size:13px;color:var(--red);text-decoration:underline}
.promo .lamp{position:absolute;left:415px;top:200px;width:410px;height:295px;background:radial-gradient(ellipse at 45% 55%,#fafafa 0%,#e6e6ea 60%,#fff 100%)}

.prod-title{left:113px;top:2272px;font-size:27px;font-weight:700}
.tabs-line{left:413px;top:2286px;width:672px;height:1px;background:#999}
.tabs{left:498px;top:2268px;width:388px;height:36px;background:#fff;border:1.5px solid #888;border-radius:3px;clip-path:polygon(4% 0,96% 0,100% 50%,96% 100%,4% 100%,0 50%);display:flex;align-items:center;justify-content:center;gap:22px;font-size:13px}
.arrows{left:1018px;top:2268px;width:68px;height:36px;background:#fff;border:1.5px solid #888;clip-path:polygon(20% 0,80% 0,100% 50%,80% 100%,20% 100%,0 50%);display:flex;align-items:center;justify-content:center;gap:14px}
.prod{position:absolute;top:2345px;width:231px;height:317px;border:2px solid #e6e6e6;background:#fff}
.prod .n{position:absolute;left:16px;top:20px;right:10px;font-size:13px;color:#444;line-height:16.5px}
.prod .img{position:absolute;left:36px;top:84px;width:158px;height:158px;border-radius:6px}
.prod .old{position:absolute;left:16px;top:266px;font-size:12.5px;color:var(--red);text-decoration:line-through}
.prod .p{position:absolute;left:16px;top:282px;font-size:17px;font-weight:700}

.news{position:absolute;left:0;top:2796px;width:1200px;height:92px;background:var(--yellow)}
.news h2{position:absolute;left:112px;top:20px;font-size:27px;font-weight:700}
.news p{position:absolute;left:112px;top:57px;font-size:12.5px;font-weight:700}
.news .in{position:absolute;left:570px;top:41px;width:384px;height:37px;background:#fff;font-size:12.5px;color:#aaa;padding:12px 18px}
.news .sub{position:absolute;left:960px;top:41px;width:129px;height:37px;background:var(--red);color:#fff;font-size:13px;font-weight:700;display:flex;align-items:center;justify-content:center}

.footer{position:absolute;left:0;top:2888px;width:1200px;height:277px;background:var(--blue);color:#fff}
.footer h5{position:absolute;top:42px;font-size:17.5px;font-weight:700}
.footer .col{position:absolute;top:100px;font-size:12.5px;line-height:16.5px}
.footer .soc{position:absolute;left:116px;top:216px;display:flex;gap:14px}
.bottom{position:absolute;left:0;top:3165px;width:1200px;height:54px;background:#fff}
.bottom .c{position:absolute;left:112px;top:28px;font-size:12.5px;color:#444}
.pay{position:absolute;top:16px;height:28px;background:#e9eef4;border-radius:3px;font-size:11px;font-weight:700;color:var(--blue);display:flex;align-items:center;justify-content:center}
</style>
</head>
<body>

<div class="topbar">
  <a class="abs login">Login/Register</a>
  <span class="abs lang">EN</span>
  <span class="abs sep"></span>
  <div class="abs social"><span class="dot red"></span><span class="dot"></span><span class="dot"></span><span class="dot"></span><span class="dot"></span></div>
</div>

<header class="header">
  <div class="abs logo"><span class="mark"></span><span class="name">CRATEVENDO</span></div>
  <nav class="abs nav"><a class="active">HOME</a><a>PRODUCTS</a><a>SERVICES</a><a>ABOUT US</a><a>BLOGS</a><a>CONTACT US</a></nav>
  <div class="abs assist">
    <svg width="48" height="42" viewBox="0 0 48 42"><circle cx="24" cy="21" r="18" fill="none" stroke="#d9221c" stroke-width="3"/><path d="M14 20c0-7 5-11 10-11s10 4 10 11" fill="none" stroke="#d9221c" stroke-width="3"/><rect x="11" y="19" width="6" height="9" rx="2" fill="#d9221c"/><rect x="31" y="19" width="6" height="9" rx="2" fill="#d9221c"/></svg>
    <div class="t">Assistance<b>02/55510420</b></div>
  </div>
</header>

<div class="catbar">
  <div class="abs allcat">
    <svg width="22" height="14" viewBox="0 0 22 14"><path d="M0 1h22M0 7h22M0 13h14" stroke="#111" stroke-width="2"/></svg>
    ALL CATEGORIES
  </div>
  <div class="abs search">Search Product</div>
  <div class="abs searchcat">Category ⌄</div>
  <div class="abs searchbtn"><svg width="18" height="18" viewBox="0 0 18 18"><circle cx="7.5" cy="7.5" r="5.5" fill="none" stroke="#fff" stroke-width="2"/><path d="M11.5 11.5l5 5" stroke="#fff" stroke-width="2"/></svg></div>
  <div class="abs icons">
    <svg width="20" height="18" viewBox="0 0 20 18"><path d="M10 17L2 9a4.5 4.5 0 016.5-6.3L10 4.2l1.5-1.5A4.5 4.5 0 0118 9z" fill="none" stroke="#fff" stroke-width="1.8"/></svg>
    <span style="display:flex;gap:6px;align-items:center"><svg width="22" height="18" viewBox="0 0 22 18"><path d="M1 1h3l3 11h11l2-8H6" fill="none" stroke="#fff" stroke-width="1.6"/><circle cx="8" cy="16" r="1.5" fill="#fff"/><circle cx="16" cy="16" r="1.5" fill="#fff"/></svg>$0.00</span>
  </div>
</div>

<section class="hero" role="img" aria-label="Blue plastic water tanks splashing in sea water on a tiled background">
  <div class="tanks"></div>
  <h1>PLASTIC TANKS</h1>
  <span class="abs from">Starting from</span>
  <div class="abs pricebox">€133.<sup>00</sup></div>
  <a class="abs btn">See All Models</a>
</section>

<section class="grey">
  <div class="feature" style="left:113px">
    <svg width="60" height="42" viewBox="0 0 60 42"><path d="M14 6h26v24H14zM40 14h10l6 8v8H40" fill="none" stroke="#111" stroke-width="2.5"/><circle cx="22" cy="33" r="4" fill="#fff" stroke="#111" stroke-width="2.5"/><circle cx="48" cy="33" r="4" fill="#fff" stroke="#111" stroke-width="2.5"/><path d="M2 12h10M4 18h8M6 24h6" stroke="#111" stroke-width="2.5"/><path d="M44 16h5l4 6h-9z" fill="#fdd000"/></svg>
    <h3>Fast Shipping</h3><p>Deleveries throughout Italy</p>
  </div>
  <div class="feature" style="left:360px">
    <svg width="56" height="50" viewBox="0 0 56 50"><path d="M12 26v-6a16 16 0 0132 0v6" fill="none" stroke="#111" stroke-width="2.5"/><rect x="8" y="24" width="8" height="14" rx="3" fill="#fdd000" stroke="#111" stroke-width="2.5"/><rect x="40" y="24" width="8" height="14" rx="3" fill="#fdd000" stroke="#111" stroke-width="2.5"/><path d="M44 38c0 6-6 8-12 8" fill="none" stroke="#111" stroke-width="2.5"/></svg>
    <h3>Customer Service</h3><p>From 9:00 to 13:00<br>02/55510420</p>
  </div>
  <div class="feature" style="left:607px">
    <svg width="50" height="50" viewBox="0 0 50 50"><path d="M8 4h28v42H8z" fill="none" stroke="#111" stroke-width="2.5"/><path d="M14 14h16M14 20h16M14 26h10" stroke="#111" stroke-width="2"/><path d="M36 28l3 6 6 1-4 4 1 6-6-3-6 3 1-6-4-4 6-1z" fill="#fdd000" stroke="#111" stroke-width="2"/></svg>
    <h3>Certified Products</h3><p>Guaranteed of quality &amp; in accordance with the law</p>
  </div>
  <div class="feature" style="left:855px">
    <svg width="50" height="44" viewBox="0 0 50 44"><rect x="8" y="6" width="38" height="24" rx="3" fill="none" stroke="#111" stroke-width="2.5"/><path d="M8 13h38" stroke="#111" stroke-width="3"/><path d="M4 24l9-4 9 4v8c0 6-5 9-9 10-4-1-9-4-9-10z" fill="#fdd000" stroke="#111" stroke-width="2.5"/></svg>
    <h3>Secure Paymets</h3><p>Credit Cards, Bank<br>Transfer, Cash on Delivery</p>
  </div>

  <h2 class="sect-title" style="top:265px">FEATURE CATEGORIES</h2>

  <div class="cat" style="left:112px;top:323px;width:386px;height:502px">
    <h4>METAL CONTAINERS</h4>
    <ul><li>Tinplate Cans</li><li>Bucket and Tipper Containers</li><li>Metal Drums</li><li>Metal containers with opening bottom</li><li>Industrial containers in sheet metal &amp; mash</li></ul>
    <a class="va" style="top:166px">VIEW ALL</a>
    <div class="ph" role="img" aria-label="Orange metal tipping container with tinplate cans" style="left:110px;top:242px;width:274px;height:258px;background:linear-gradient(135deg,#f26a2a 0%,#e35b1f 60%,#b9babd 61%,#d6d7d9 100%)"></div>
  </div>
  <div class="cat" style="left:514px;top:323px;width:314px;height:244px">
    <h4 style="left:20px">PLASIC CONTAINERS</h4>
    <ul style="left:18px"><li>Plastic jars</li><li>Plastic Tipping Buckets</li><li>Plastic Bins &amp; drums</li><li>Plastic bottles</li><li>Plastic pallet Crates</li></ul>
    <a class="va" style="left:18px;top:166px">VIEW ALL</a>
    <div class="ph" role="img" aria-label="Blue plastic tanks and a pallet tank" style="left:158px;top:88px;width:154px;height:154px;border-radius:40px 0 0 0;background:linear-gradient(160deg,#3a9be8,#1467c4 70%,#d6d6d6 100%)"></div>
  </div>
  <div class="cat" style="left:514px;top:584px;width:314px;height:241px">
    <h4 style="left:16px">TECHNICAL FURNITURE</h4>
    <ul style="left:18px"><li>Work Clothes &amp; PPE</li><li>Work Gloves</li><li>Safety Shoes</li><li>Respiratory Protection</li><li>Head Protection</li><li>Eye Protection</li></ul>
    <a class="va" style="left:18px;top:178px">VIEW ALL</a>
    <div class="ph" role="img" aria-label="Safety helmet, ear defenders, gloves and goggles" style="left:160px;top:108px;width:152px;height:131px;border-radius:60px 0 0 0;background:linear-gradient(150deg,#f07c1a,#f3c52a 55%,#e8e8e8 100%)"></div>
  </div>
  <div class="cat" style="left:842px;top:323px;width:242px;height:502px">
    <h4 style="left:18px">TECHNICAL FURNITURE</h4>
    <ul style="left:18px"><li>Wardrobs</li><li>Work benches &amp; table</li><li>Drawers, Filing Cabinets &amp; Cartelliere</li><li>Visual Communication</li><li>Benches for changing rooms</li><li>Screens &amp; Partion Walls</li></ul>
    <a class="va" style="left:18px;top:182px">VIEW ALL</a>
    <div class="ph" role="img" aria-label="Grey metal locker and blue workbench" style="left:0;top:232px;width:240px;height:268px;background:linear-gradient(180deg,#c9cbce 0%,#b5b8bb 55%,#2c6fb0 56%,#1d5c9c 100%)"></div>
  </div>

  <a class="btn-red" style="left:514px;top:862px;width:169px;height:34px">VIEW ALL CATEGORIES</a>
</section>

<section class="promo">
  <div class="side" style="left:0" role="img" aria-label="UV disinfection lamp with keys under violet light"></div>
  <div class="side" style="left:831px" role="img" aria-label="UV disinfection lamp with eyeglasses"></div>
  <div class="save">SAVE NOW</div>
  <div class="sub">Rechargeable UV Disinfection Lamp, In ABS, Table</div>
  <div class="off"><span class="s">UPTO</span><span class="b">25%</span><span class="s">OFF</span></div>
  <a class="shop">SHOP NOW</a>
  <div class="lamp" role="img" aria-label="White UV disinfection table lamp"></div>
</section>

<h2 class="abs prod-title">FEATURE PRODUCTS</h2>
<div class="abs tabs-line"></div>
<div class="abs tabs"><span>NEW ARRIVAL</span><span>-</span><span>BEST SELLER</span><span>-</span><span>SPECIAL</span></div>
<div class="abs arrows"><svg width="8" height="12" viewBox="0 0 8 12"><path d="M7 1L2 6l5 5" fill="none" stroke="#555" stroke-width="1.6"/></svg><svg width="8" height="12" viewBox="0 0 8 12"><path d="M1 1l5 5-5 5" fill="none" stroke="#555" stroke-width="1.6"/></svg></div>

<div class="prod" style="left:113px"><div class="n">Plastic Bottles (HDPE), Square<br>Wide Neck, Screw Cap (Included)</div><div class="img" role="img" aria-label="White square plastic bottles with red caps" style="background:linear-gradient(180deg,#f3f3f3,#e2e2e2)"></div><div class="old">€ 8,36</div><div class="p">€7,94</div></div>
<div class="prod" style="left:362px"><div class="n">Mobile Drawer With 6 Drawers,<br>Orange Colour</div><div class="img" role="img" aria-label="Orange mobile tool drawer cabinet" style="background:linear-gradient(180deg,#f26a2a,#c9501c)"></div><div class="old">€ 1.049,20</div><div class="p">€647,88</div></div>
<div class="prod" style="left:608px"><div class="n">Folding Anti-Noise Headphone,<br>DB MIT 29 SNR, EN 352-1<br>Certified</div><div class="img" role="img" aria-label="Black and yellow folding ear defenders" style="background:linear-gradient(180deg,#4a4a4a,#2a2a2a)"></div><div class="old">€ 16,60</div><div class="p">€11,63</div></div>
<div class="prod" style="left:855px"><div class="n">Tipping &amp; Forkable Steel Buckets,<br>Loading with mulet,<br>without wheels</div><div class="img" role="img" aria-label="Orange steel tipping skip" style="background:linear-gradient(180deg,#f47a2e,#d95a18)"></div><div class="old">€ 901,82</div><div class="p">€676,37</div></div>

<a class="btn-red" style="left:550px;top:2697px;width:97px;height:33px">VIEW ALL</a>

<section class="news">
  <h2>NEWSLETTER</h2>
  <p>Subscribe to our newsletter to stay up to date on news and promotions!</p>
  <div class="in">Enter your email address</div>
  <a class="sub">SUBSCRIBE</a>
</section>

<footer class="footer">
  <h5 style="left:112px">CRATEVENDO SRL</h5>
  <h5 style="left:571px">CONTACTS</h5>
  <h5 style="left:752px">INFORMATION</h5>
  <h5 style="left:991px">SERVICES</h5>
  <div class="col" style="left:115px;width:380px">Plastic &nbsp;Containers, Metal Containers, Shelves, Lockers, Safety &amp; Environment, &nbsp;Pallets And Benches, &nbsp;Packaging Products, First Aid, Accident Prevention and PPE &nbsp;Delivery in 24 / 48H throughout Italy. Products at the &nbsp;best price, &nbsp;for the proper functioning of every institution and company.</div>
  <div class="col" style="left:574px">Contacts<br>Who we are<br>Certifications<br>Announcements<br>Site map</div>
  <div class="col" style="left:755px">Info Privacy<br>Info Cookies<br>Terms and<br>Conditions of Sale<br>Payment methods<br>Shipping and<br>Withdrawals</div>
  <div class="col" style="left:994px">Online quote<br>FAQs<br>Guides and Tips<br>Catalogs<br>Regulations<br>Materials</div>
  <div class="soc"><span class="dot red"></span><span class="dot"></span><span class="dot"></span><span class="dot"></span><span class="dot"></span></div>
</footer>

<div class="bottom">
  <span class="c">CRATEVENDO Srl © 2021 ALL RIGHTS RESERVED</span>
  <div class="pay" style="left:820px;width:84px">Paywise</div>
  <div class="pay" style="left:914px;width:100px;background:#eee"></div>
  <div class="pay" style="left:1024px;width:62px;font-size:9px">Bank Transfer</div>
</div>

</body>
</html>
```